Need Bold, Hip Card for Concert Ticket Website Gleaming Passes!

Hi there! I am putting together a business/website that sells event tickets (mostly concerts, but also some sports and theater). Think SeatNook, but much smaller. The site is called Gleaming Passes. I have a new logo (attached, with black/red/white color scheme), and am looking for a modern/cool/original business card design. Note that I am thinking of having the card itself in the shape of a ticket (die cut), so you may want to keep that in mind when designing, but I'm not set on that. I'm also open to alternative card sizes, thicknesses, glossy, spot UV, etc. in order to stand out. I'm attaching a potential die cut template and a sample card using that template in case you want to work with that.
Target Market(s)
Music fans, people that like going to see live events
Industry/Entity Type
Entertainment
Contact Information for Business Card
Information that I'd like to have:
website address - www.gleamingpasses.example
phone number: 1-833-5GLEAMNG (532-6264)
my name - Wendel Pike

```html
<!DOCTYPE html>
<html lang="en">
<head>
<meta charset="utf-8">
<title>Gleaming Passes – Business Card</title>
<link rel="stylesheet" href="https://fonts.googleapis.com/css2?family=Montserrat:wght@700&family=Roboto+Condensed:wght@400;700&display=swap">
<style>
  :root {
    --stage: #2a2a2a;
    --ticket-red: #8e0d14;
    --ticket-red-light: #a8232b;
    --ticket-white: #ffffff;
    --ink: #1d1d1d;
    --rule-light: rgba(255,255,255,0.85);
    --rule-dark: #2a2a2a;
  }
  * { box-sizing: border-box; margin: 0; padding: 0; }
  html, body { width: 1200px; height: 900px; overflow: hidden; }
  body { background: var(--stage); position: relative; font-family: "Roboto Condensed", Arial, sans-serif; }

  .ticket { position: absolute; top: 321px; height: 258px; }
  .ticket-shape { position: absolute; inset: 0; width: 100%; height: 100%; }
  .ticket--front { left: 72px; width: 515px; }
  .ticket--back { left: 648px; width: 482px; }

  /* Front */
  .front-divider { position: absolute; left: 253px; top: 19px; width: 1px; height: 219px; background: var(--rule-light); }
  .front-rule { position: absolute; left: 266px; width: 208px; height: 1px; background: var(--rule-light); }
  .front-rule--top { top: 80px; }
  .front-rule--bottom { top: 175px; }
  .front-name {
    position: absolute; left: 266px; width: 208px; top: 96px;
    font-family: "Montserrat", Arial, sans-serif; font-weight: 700; color: var(--ticket-white);
    text-transform: uppercase; text-align: center; line-height: 1.05; font-size: 30px;
  }
  .front-name span { display: block; }
  .front-web {
    position: absolute; left: 266px; width: 208px; top: 196px; text-align: center;
    color: var(--ticket-white); font-size: 13px; letter-spacing: 0.3px; text-transform: uppercase;
  }
  .front-web b { font-weight: 700; }

  /* Back */
  .back-frame { position: absolute; left: 23px; top: 31px; width: 401px; height: 195px; border: 1px solid var(--rule-dark); }
  .back-brand {
    position: absolute; left: 0; right: 0; top: 58px; display: flex; justify-content: center; align-items: center; gap: 12px;
  }
  .back-brand-mark { width: 30px; height: 30px; background: var(--ticket-red); }
  .back-brand-name {
    font-family: "Montserrat", Arial, sans-serif; font-weight: 700; color: var(--ticket-red);
    font-size: 30px; text-transform: uppercase; line-height: 1;
  }
  .back-rule { position: absolute; left: 42px; width: 363px; height: 1px; background: var(--rule-dark); }
  .back-rule--top { top: 148px; }
  .back-rule--bottom { top: 186px; }
  .back-person {
    position: absolute; left: 42px; width: 363px; top: 159px; text-align: center;
    font-size: 11.5px; color: var(--ink); text-transform: uppercase; letter-spacing: 0.2px;
  }
  .back-person b { font-weight: 700; }
  .back-contact {
    position: absolute; left: 42px; width: 363px; top: 197px; display: flex; justify-content: center; align-items: center;
    font-size: 11px; color: var(--ink); text-transform: uppercase;
  }
  .back-contact-sep { width: 1px; height: 18px; background: var(--rule-dark); margin: 0 8px; }
</style>
</head>
<body>

<section class="ticket ticket--front" aria-label="Card front">
  <svg class="ticket-shape" viewBox="0 0 515 258" aria-hidden="true">
    <defs>
      <linearGradient id="front-sheen" x1="0" y1="0" x2="1" y2="1">
        <stop offset="0" stop-color="#a8232b" stop-opacity="0.55"/>
        <stop offset="0.6" stop-color="#b8323a" stop-opacity="0.35"/>
        <stop offset="1" stop-color="#8e0d14" stop-opacity="0"/>
      </linearGradient>
      <clipPath id="front-clip">
        <path d="M30 0 H485 A30 30 0 0 0 515 30 V107 A22 22 0 0 0 515 151 V228 A30 30 0 0 0 485 258 H30 A30 30 0 0 0 0 228 V151 A22 22 0 0 0 0 107 V30 A30 30 0 0 0 30 0 Z"/>
      </clipPath>
    </defs>
    <path fill="#8e0d14" d="M30 0 H485 A30 30 0 0 0 515 30 V107 A22 22 0 0 0 515 151 V228 A30 30 0 0 0 485 258 H30 A30 30 0 0 0 0 228 V151 A22 22 0 0 0 0 107 V30 A30 30 0 0 0 30 0 Z"/>
    <rect x="0" y="0" width="245" height="258" fill="url(#front-sheen)" clip-path="url(#front-clip)" role="img" aria-label="Soft glossy sheen panel"/>
  </svg>
  <div class="front-divider"></div>
  <div class="front-rule front-rule--top"></div>
  <h1 class="front-name"><span>Gleaming</span><span>Passes</span></h1>
  <div class="front-rule front-rule--bottom"></div>
  <p class="front-web">www.<b>gleamingpasses</b>.example</p>
</section>

<section class="ticket ticket--back" aria-label="Card back">
  <svg class="ticket-shape" viewBox="0 0 482 258" aria-hidden="true">
    <path fill="#ffffff" d="M30 0 H452 A30 30 0 0 0 482 30 V107 A22 22 0 0 0 482 151 V228 A30 30 0 0 0 452 258 H30 A30 30 0 0 0 0 228 V151 A22 22 0 0 0 0 107 V30 A30 30 0 0 0 30 0 Z"/>
  </svg>
  <div class="back-frame"></div>
  <div class="back-brand">
    <span class="back-brand-mark"></span>
    <span class="back-brand-name">Gleaming Passes</span>
  </div>
  <div class="back-rule back-rule--top"></div>
  <p class="back-person"><b>Wendel Pike</b> | Managing Director</p>
  <div class="back-rule back-rule--bottom"></div>
  <p class="back-contact">
    <span class="back-contact-phone">1-833-5GLEAMNG (532-6264)</span>
    <span class="back-contact-sep"></span>
    <span class="back-contact-email">wendelpike@gleamingpasses.example</span>
  </p>
</section>

</body>
</html>
```